Harbor Business Cards

I need a business card designed with the following information.

Company Name: Harbor Wealth Management
Name: BriAnne Dockery
Title: Executive Assistant
Cell: (281) 555-0173
Direct Line: (832) 555-0148
Email: brianne@harborwmx.com
Address: 20537 W. Marlowe PKWY Ste. B
Tomball, TX 77390

I have attached the logo.
I would like it in navy blue and silver.
Thanks.

```html
<!DOCTYPE html>
<html lang="en">
<head>
<meta charset="utf-8">
<title>Harbor Wealth Management – Business Card</title>
<link rel="stylesheet" href="https://fonts.googleapis.com/css2?family=Open+Sans:wght@400;600&display=swap">
<style>
  :root {
    --navy: #1c2a3f;
    --silver: #e6e9ed;
    --silver-edge: #cfd4da;
    --ink-soft: #3a4658;
    --backdrop: #f3f4f6;
  }
  html, body {
    margin: 0;
    width: 1200px;
    height: 1047px;
    overflow: hidden;
    background: var(--backdrop);
    font-family: "Open Sans", Arial, sans-serif;
  }
  .card {
    position: absolute;
    left: 130px;
    top: 266px;
    width: 940px;
    height: 515px;
    background: var(--silver);
    border: 1px solid var(--silver-edge);
    border-radius: 28px;
    overflow: hidden;
    color: var(--navy);
  }
  .brand-mark {
    position: absolute;
    left: 118px;
    top: 32px;
    width: 84px;
    height: 84px;
    background: var(--navy);
  }
  .brand-name {
    position: absolute;
    left: 29px;
    top: 148px;
    width: 265px;
    text-align: center;
    font-weight: 400;
    color: var(--navy);
    line-height: 1;
  }
  .brand-name .line-main {
    display: block;
    font-size: 30px;
    letter-spacing: 8px;
  }
  .brand-name .line-sub {
    display: block;
    margin-top: 10px;
    font-size: 11.5px;
    letter-spacing: 2.6px;
  }
  .name-tab {
    position: absolute;
    left: 0;
    top: 228px;
    width: 10px;
    height: 54px;
    background: var(--navy);
    border-radius: 0 8px 8px 0;
  }
  .person-name {
    position: absolute;
    left: 32px;
    top: 222px;
    margin: 0;
    font-size: 38px;
    font-weight: 600;
    line-height: 1.1;
  }
  .person-title {
    position: absolute;
    left: 32px;
    top: 265px;
    margin: 0;
    font-size: 23px;
    color: var(--ink-soft);
  }
  .address {
    position: absolute;
    left: 32px;
    top: 306px;
    margin: 0;
    font-style: normal;
    font-size: 21px;
    line-height: 30px;
    color: var(--ink-soft);
  }
  .contacts {
    position: absolute;
    left: 32px;
    top: 378px;
    margin: 0;
    padding: 0;
    list-style: none;
    font-size: 20.5px;
    line-height: 27.5px;
    color: var(--ink-soft);
  }
  .contacts li {
    display: flex;
    align-items: center;
    gap: 8px;
  }
  .contacts svg {
    width: 18px;
    height: 18px;
    fill: var(--navy);
    flex: none;
  }
  .feature-mark {
    position: absolute;
    left: 478px;
    top: 58px;
    width: 400px;
    height: 400px;
    background: var(--navy);
  }
</style>
</head>
<body>
  <div class="card">
    <div class="brand-mark"></div>
    <div class="brand-name">
      <span class="line-main">HARBOR</span>
      <span class="line-sub">WEALTH MANAGEMENT</span>
    </div>

    <div class="name-tab"></div>
    <h1 class="person-name">BriAnne Dockery</h1>
    <p class="person-title">Executive Assistant</p>

    <address class="address">
      20537 W. Marlowe PKWY Ste. B<br>
      Tomball, TX 77390
    </address>

    <ul class="contacts">
      <li>
        <svg viewBox="0 0 16 16" aria-hidden="true"><path d="M4 0h8a1.5 1.5 0 0 1 1.5 1.5v13A1.5 1.5 0 0 1 12 16H4a1.5 1.5 0 0 1-1.5-1.5v-13A1.5 1.5 0 0 1 4 0zm0.5 2v10.5h7V2zm3.5 11.3a.9.9 0 1 0 0 1.8.9.9 0 0 0 0-1.8z"/></svg>
        (281) 555-0173
      </li>
      <li>
        <svg viewBox="0 0 16 16" aria-hidden="true"><path d="M3.6 1.2l2.2 2.9-1.3 1.6c.9 2 2.5 3.6 4.5 4.6l1.6-1.3 2.9 2.2-1.4 2.6C6.8 13.5 2.4 9 1.1 3z"/></svg>
        (832) 555-0148
      </li>
      <li>
        <svg viewBox="0 0 16 16" aria-hidden="true"><path d="M1 3h14v10H1zm1.5 1.4v.3L8 8.4l5.5-3.7v-.3zm0 2v5.1h11V6.4L8 10.1z"/></svg>
        brianne@harborwmx.com
      </li>
      <li>
        <svg viewBox="0 0 16 16" aria-hidden="true"><path d="M8 1a7 7 0 1 0 0 14A7 7 0 0 0 8 1zm0 1.5c.8 0 1.8 1.7 2.1 4.3H5.9C6.2 4.2 7.2 2.5 8 2.5zM2.6 8.2h2.2c0 1.6.3 3 .8 4.1a5.6 5.6 0 0 1-3-4.1zm0-1.4a5.6 5.6 0 0 1 3-4.1c-.5 1.1-.8 2.5-.8 4.1zm5.4 6.7c-.8 0-1.8-1.7-2.1-5.3h4.2c-.3 3.6-1.3 5.3-2.1 5.3zm2.4-1.2c.5-1.1.8-2.5.8-4.1h2.2a5.6 5.6 0 0 1-3 4.1zm.8-5.5c0-1.6-.3-3-.8-4.1a5.6 5.6 0 0 1 3 4.1z"/></svg>
        www.harborwmx.com
      </li>
    </ul>

    <div class="feature-mark" role="img" aria-label="Large navy brand emblem area"></div>
  </div>
</body>
</html>
```